New ecommerce website needed for Epoxy Retailer

We need a new shopify website designed and built for our epoxy supply store.
We sell Epoxy, wood, epoxy furniture, supplies and provide classes on how to use epoxy.
We are looking for a website with a home page and 7 primary navigation links at the top. Some of these links should have a drop down menu with the below listed pages linked to them...
Sub Pages:
- Glacier Resin
- Epoxy
- Pigments
- Heron Balm
- Molds
- Silicone
- HDPE
- Wood
- Live Edge
- Ovals & Rounds
- Pre-cut
- Charcuterie Wood
- Custom Milling
- Wholesale
- Supplies
- Furniture
-Education
- In person workshops
- My courses (are we able to have a login section for customers to see their purchases?)
- About Us

```html
<!DOCTYPE html>
<html lang="en">
<head>
<meta charset="utf-8">
<title>Timberpour Studio – Epoxy Supply Store</title>
<link href="https://fonts.googleapis.com/css2?family=Bebas+Neue&family=Poppins:wght@400;500;600;700&display=swap" rel="stylesheet">
<style>
:root{
  --red:#ec5f52;
  --ink:#1d1d1d;
  --black:#0c0c0c;
  --grey:#efefef;
  --mid:#8a8a8a;
  --pink:#fbe2e1;
  --footer:#2e2e2e;
  --white:#ffffff;
}
*{box-sizing:border-box;margin:0;padding:0}
html,body{width:1200px;height:4608px;overflow:hidden;background:var(--white)}
body{font-family:"Poppins",sans-serif;color:var(--ink)}
.page{position:relative;width:1200px;height:4608px;overflow:hidden}
.abs{position:absolute}
ul{list-style:none}

/* top bar */
.topbar{top:0;left:0;width:1200px;height:32px;font-size:8px;font-weight:500}
.topbar span{position:absolute;top:11px}
.topbar .sep{position:absolute;top:8px;width:1px;height:16px;background:#999}
.topbar .call{left:799px;top:6px;line-height:9px;font-size:7px}
.topbar .call b{font-size:9px;font-weight:600}

/* header */
.header{top:32px;left:0;width:1200px;height:77px}
.search{position:absolute;left:111px;top:22px;width:331px;height:33px;border:1px solid #d8d8d8;border-radius:17px;font-size:8px;font-weight:600;padding:10px 22px}
.search svg{position:absolute;right:16px;top:8px}
.brand{position:absolute;left:540px;top:8px;width:120px;height:62px;display:flex;flex-direction:column;align-items:center;justify-content:center;font-family:"Bebas Neue",sans-serif;color:var(--ink);font-size:26px;line-height:22px;text-align:center}
.store-btn{position:absolute;left:760px;top:21px;width:161px;height:34px;border:2px solid var(--red);border-radius:17px;color:var(--red);font-size:10px;font-weight:600;display:flex;align-items:center;justify-content:center;gap:6px}
.header .icon{position:absolute;top:22px}
.cart-dot{position:absolute;left:1074px;top:22px;width:9px;height:9px;border-radius:50%;background:var(--red)}

/* nav */
.nav{top:109px;left:0;width:1200px;height:43px;background:var(--black)}
.nav ul{position:absolute;left:195px;width:730px;top:0;height:43px;display:flex;justify-content:space-around;align-items:center}
.nav li{font-family:"Bebas Neue",sans-serif;color:var(--white);font-size:15px;letter-spacing:.4px}
.burger{position:absolute;left:948px;top:0;width:41px;height:43px;background:var(--red);display:flex;flex-direction:column;justify-content:center;align-items:center;gap:4px}
.burger i{display:block;width:18px;height:2px;background:var(--white)}

/* hero */
.hero{top:152px;left:0;width:1200px;height:581px;background:linear-gradient(180deg,#6f8ea7 0%,#b9a78d 30%,#e2a24c 46%,#6d6a58 56%,#b6865a 64%,#8a5d36 100%)}
.hero h1{position:absolute;left:109px;top:160px;font-family:"Bebas Neue",sans-serif;color:var(--white);font-size:67px;line-height:64px;font-weight:400;letter-spacing:.5px}
.btn{position:absolute;background:var(--red);color:var(--white);font-family:"Bebas Neue",sans-serif;border-radius:24px;display:flex;align-items:center;justify-content:center;letter-spacing:.6px}
.hero .btn{left:111px;top:392px;width:168px;height:44px;font-size:18px}

/* product shelves */
.shelf{left:0;width:1200px}
.shelf.grey{background:var(--grey)}
.shelf h2{position:absolute;left:0;width:1200px;top:62px;text-align:center;font-family:"Bebas Neue",sans-serif;font-size:34px;font-weight:400;letter-spacing:.3px}
.rule{position:absolute;left:492px;top:108px;width:216px;height:16px}
.cards{position:absolute;left:111px;top:143px;width:978px;height:268px;display:flex;justify-content:space-between}
.card{width:218px;height:268px;background:var(--white);border-radius:100px 100px 0 0;position:relative;text-align:center}
.shelf.white .card{background:var(--grey)}
.card .shot{position:absolute;left:59px;top:44px;width:100px;height:115px;border-radius:10px}
.card .name{position:absolute;left:0;width:218px;top:180px;font-size:10.5px;font-weight:700}
.card .row{position:absolute;left:0;width:218px;top:212px;display:flex;justify-content:center;align-items:center;gap:12px;font-size:10px}
.card .pill{border:1.5px solid var(--red);border-radius:12px;width:75px;height:24px;font-size:8px;display:flex;align-items:center;justify-content:center}
.arrow{position:absolute;top:267px;width:28px;height:28px}
.shelf .btn{left:515px;top:439px;width:168px;height:44px;font-size:19px}

.s-resin{background:linear-gradient(160deg,#5a5d62,#9aa3b5 45%,#2a4fb0)}
.s-pig{background:linear-gradient(160deg,#2c2c2c,#c72d2d 60%,#111)}
.s-jug{background:linear-gradient(160deg,#f3f3f3,#cfd6e3 60%,#6a7fb3)}
.s-blue{background:linear-gradient(160deg,#2f61c9,#8fb3ef 60%,#1c3e92)}
.s-oil{background:linear-gradient(160deg,#111,#3a3a3a 60%,#d9d9d9)}
.s-tin{background:radial-gradient(circle,#d9d9d9,#8c8c8c)}
.s-wax{background:radial-gradient(circle,#3c3c3c,#111)}
.s-dark{background:linear-gradient(160deg,#3a2c22,#5c4638 50%,#2a2622)}
.s-light{background:linear-gradient(160deg,#e6c28a,#c79453)}
.s-walnut{background:linear-gradient(160deg,#6d3519,#8f4826)}
.s-oak{background:linear-gradient(160deg,#b98b54,#7e5328)}
.s-board1{background:linear-gradient(160deg,#efd9b0,#d7b680)}
.s-board2{background:linear-gradient(160deg,#9c5a2a,#5c3015)}
.s-board3{background:linear-gradient(160deg,#d49a58,#9c5a24)}
.s-board4{background:linear-gradient(160deg,#f0b36a,#cf8438)}
.shot.slab{left:34px;top:60px;width:150px;height:75px;border-radius:6px}
.shot.tin{left:54px;top:54px;width:110px;height:110px;border-radius:50%}

/* video */
.video-band{top:3295px;left:0;width:1200px;height:483px;background:var(--grey)}
.video{top:3011px;left:111px;width:978px;height:628px;border-radius:24px;background:linear-gradient(150deg,#b8a995 0%,#ddd0bd 35%,#c89a3e 60%,#8f6a27 100%)}
.video .play{position:absolute;left:459px;top:270px;width:60px;height:60px}
.video p{position:absolute;left:0;width:978px;top:355px;text-align:center;font-family:"Bebas Neue",sans-serif;color:var(--white);font-size:30px;letter-spacing:.5px}

/* testimonials */
.testi{top:3778px;left:0;width:1200px;height:427px;background:var(--pink);text-align:center}
.testi h2{position:absolute;left:0;width:1200px;top:60px;font-family:"Bebas Neue",sans-serif;font-size:54px;font-weight:400;letter-spacing:.5px;line-height:54px}
.testi h3{position:absolute;left:0;width:1200px;top:128px;font-size:24px;font-weight:500;letter-spacing:1.2px}
.testi blockquote{position:absolute;left:360px;width:480px;top:178px;font-size:9px;line-height:17px;color:#444}
.testi blockquote b{color:var(--red);font-size:16px}
.testi .who{position:absolute;left:0;width:1200px;top:249px;font-size:7.5px;font-weight:700}
.avatar{position:absolute;left:577px;top:277px;width:46px;height:46px;border-radius:50%;background:linear-gradient(160deg,#e6c2b4,#b58b7c)}
.dots{position:absolute;left:568px;top:349px;display:flex;gap:8px}
.dots i{width:9px;height:9px;border-radius:50%;background:#e7c9c7}
.dots i:first-child{background:var(--red)}
.testi .arrow{top:194px}

/* footer */
.footer{top:4205px;left:0;width:1200px;height:403px;background:var(--footer);color:var(--white)}
.footer .brand{left:105px;top:58px;width:130px;height:120px;color:var(--white);font-size:30px;line-height:26px}
.footer .brand i{display:block;width:14px;height:14px;border-radius:50%;background:var(--white);margin-top:8px}
.follow{position:absolute;left:110px;top:207px;width:120px;text-align:center;font-family:"Bebas Neue",sans-serif;font-size:18px}
.social{position:absolute;left:110px;top:251px;display:flex;gap:10px}
.social i{width:24px;height:24px;border-radius:50%;background:var(--white)}
.social i:nth-child(2){background:var(--red)}
.col{position:absolute;top:66px}
.col h4{font-family:"Bebas Neue",sans-serif;font-size:18px;font-weight:400;margin-bottom:4px}
.col li{font-size:11px;line-height:20.5px;color:#ddd}
.col h4.more{margin-top:32px}
.contact{position:absolute;left:867px;top:66px;width:300px}
.contact h4{font-family:"Bebas Neue",sans-serif;font-size:18px;font-weight:400}
.contact .line{position:absolute;left:0;display:flex;gap:10px;font-size:11px;line-height:18px;color:#ddd}
.contact .line svg{flex:none}
.copy{position:absolute;left:0;width:1200px;top:370px;text-align:center;font-size:9px;color:#ccc}
</style>
</head>
<body>
<div class="page">

  <div class="abs topbar">
    <span style="left:134px">Select Language ⌄</span>
    <div class="sep" style="left:232px"></div>
    <span style="left:266px">Currency:USD ⌄</span>
    <svg class="abs" style="left:773px;top:8px" width="16" height="16" viewBox="0 0 24 24" fill="none" stroke="#444" stroke-width="2"><path d="M5 3h4l2 5-3 2a11 11 0 0 0 6 6l2-3 5 2v4a2 2 0 0 1-2 2A17 17 0 0 1 3 5a2 2 0 0 1 2-2z"/></svg>
    <span class="call">QUESTION? CALL US<br><b>1234567890</b></span>
    <div class="sep" style="left:913px"></div>
    <span style="left:925px">Welcome To Timberpour Studio</span>
  </div>

  <header class="abs header">
    <div class="search">Search Our Store
      <svg width="16" height="16" viewBox="0 0 24 24" fill="none" stroke="#333" stroke-width="2"><circle cx="10" cy="10" r="7"/><path d="M15 15l6 6"/></svg>
    </div>
    <div class="brand">Timberpour<br>Studio</div>
    <div class="store-btn">
      <svg width="12" height="14" viewBox="0 0 24 28" fill="none" stroke="#ec5f52" stroke-width="3"><path d="M12 26s9-9 9-15a9 9 0 0 0-18 0c0 6 9 15 9 15z"/><circle cx="12" cy="11" r="3"/></svg>
      FIND OUR STORE
    </div>
    <svg class="icon" style="left:1007px" width="28" height="28" viewBox="0 0 28 28" fill="none" stroke="#333" stroke-width="2"><circle cx="14" cy="14" r="12"/><circle cx="14" cy="11" r="4"/><path d="M6 22c2-4 5-5 8-5s6 1 8 5"/></svg>
    <svg class="icon" style="left:1054px" width="26" height="28" viewBox="0 0 26 28" fill="none" stroke="#333" stroke-width="2"><path d="M3 9h20l-1 17H4z"/><path d="M8 9V6a5 5 0 0 1 10 0v3"/></svg>
    <div class="cart-dot"></div>
  </header>

  <nav class="abs nav">
    <ul>
      <li>About Us</li><li>My Courses</li><li>In Person Workshops</li><li>Education</li><li>Furniture</li><li>Supplies</li><li>Wholesale</li>
    </ul>
    <div class="burger"><i></i><i></i><i></i></div>
  </nav>

  <section class="abs hero" role="img" aria-label="Misty mountain sunrise over a wooden tabletop with resin and hardener jugs">
    <h1>Epoxy Supply Store<br>Forall Kind Of Wood And<br>Epoxy Furniture</h1>
    <div class="btn">Shop Now</div>
  </section>

  <!-- shelf 1 -->
  <section class="abs shelf grey" style="top:733px;height:554px">
    <h2>Glacier Resin</h2>
    <svg class="rule" viewBox="0 0 216 16"><line x1="0" y1="8" x2="92" y2="8" stroke="#ec5f52" stroke-width="1.5"/><line x1="124" y1="8" x2="216" y2="8" stroke="#ec5f52" stroke-width="1.5"/><circle cx="108" cy="8" r="8" fill="#888"/></svg>
    <svg class="arrow" style="left:52px" viewBox="0 0 28 28"><circle cx="14" cy="14" r="13" fill="#fff" stroke="#ec5f52"/><path d="M18 14H10M13 10l-4 4 4 4" stroke="#ec5f52" stroke-width="1.5" fill="none"/></svg>
    <svg class="arrow" style="left:1118px" viewBox="0 0 28 28"><circle cx="14" cy="14" r="13" fill="#fff" stroke="#ec5f52"/><path d="M10 14h8M15 10l4 4-4 4" stroke="#ec5f52" stroke-width="1.5" fill="none"/></svg>
    <div class="cards">
      <div class="card"><div class="shot s-resin" role="img" aria-label="Resin can"></div><div class="name">PRODUCT NAME</div><div class="row">$50.00<span class="pill">SHOP NOW</span></div></div>
      <div class="card"><div class="shot s-pig" role="img" aria-label="Pigment bottle"></div><div class="name">PRODUCT NAME</div><div class="row">$50.00<span class="pill">SHOP NOW</span></div></div>
      <div class="card"><div class="shot s-jug" role="img" aria-label="Epoxy jug"></div><div class="name">PRODUCT NAME</div><div class="row">$50.00<span class="pill">SHOP NOW</span></div></div>
      <div class="card"><div class="shot s-blue" role="img" aria-label="Blue mica powder"></div><div class="name">PRODUCT NAME</div><div class="row">$50.00<span class="pill">SHOP NOW</span></div></div>
    </div>
    <div class="btn">View All</div>
  </section>

  <!-- shelf 2 -->
  <section class="abs shelf white" style="top:1287px;height:551px">
    <h2>Heron Balm</h2>
    <svg class="rule" viewBox="0 0 216 16"><line x1="0" y1="8" x2="92" y2="8" stroke="#ec5f52" stroke-width="1.5"/><line x1="124" y1="8" x2="216" y2="8" stroke="#ec5f52" stroke-width="1.5"/><circle cx="108" cy="8" r="8" fill="#888"/></svg>
    <svg class="arrow" style="left:52px" viewBox="0 0 28 28"><circle cx="14" cy="14" r="13" fill="#fff" stroke="#ec5f52"/><path d="M18 14H10M13 10l-4 4 4 4" stroke="#ec5f52" stroke-width="1.5" fill="none"/></svg>
    <svg class="arrow" style="left:1118px" viewBox="0 0 28 28"><circle cx="14" cy="14" r="13" fill="#fff" stroke="#ec5f52"/><path d="M10 14h8M15 10l4 4-4 4" stroke="#ec5f52" stroke-width="1.5" fill="none"/></svg>
    <div class="cards">
      <div class="card"><div class="shot s-oil" role="img" aria-label="Oil bottle"></div><div class="name">PRODUCT NAME</div><div class="row">$50.00<span class="pill">SHOP NOW</span></div></div>
      <div class="card"><div class="shot s-oil" role="img" aria-label="Oil jerrycan"></div><div class="name">PRODUCT NAME</div><div class="row">$50.00<span class="pill">SHOP NOW</span></div></div>
      <div class="card"><div class="shot tin s-tin" role="img" aria-label="Silver wax tin"></div><div class="name">PRODUCT NAME</div><div class="row">$50.00<span class="pill">SHOP NOW</span></div></div>
      <div class="card"><div class="shot tin s-wax" role="img" aria-label="Black wood wax tin"></div><div class="name">PRODUCT NAME</div><div class="row">$50.00<span class="pill">SHOP NOW</span></div></div>
    </div>
    <div class="btn">View All</div>
  </section>

  <!-- shelf 3 -->
  <section class="abs shelf grey" style="top:1838px;height:554px">
    <h2>Live Edge</h2>
    <svg class="rule" viewBox="0 0 216 16"><line x1="0" y1="8" x2="92" y2="8" stroke="#ec5f52" stroke-width="1.5"/><line x1="124" y1="8" x2="216" y2="8" stroke="#ec5f52" stroke-width="1.5"/><circle cx="108" cy="8" r="8" fill="#888"/></svg>
    <svg class="arrow" style="left:52px" viewBox="0 0 28 28"><circle cx="14" cy="14" r="13" fill="#fff" stroke="#ec5f52"/><path d="M18 14H10M13 10l-4 4 4 4" stroke="#ec5f52" stroke-width="1.5" fill="none"/></svg>
    <svg class="arrow" style="left:1118px" viewBox="0 0 28 28"><circle cx="14" cy="14" r="13" fill="#fff" stroke="#ec5f52"/><path d="M10 14h8M15 10l4 4-4 4" stroke="#ec5f52" stroke-width="1.5" fill="none"/></svg>
    <div class="cards">
      <div class="card"><div class="shot slab s-dark" role="img" aria-label="Dark live edge slab"></div><div class="name">PRODUCT NAME</div><div class="row">$50.00<span class="pill">SHOP NOW</span></div></div>
      <div class="card"><div class="shot slab s-light" role="img" aria-label="Light live edge slab"></div><div class="name">PRODUCT NAME</div><div class="row">$50.00<span class="pill">SHOP NOW</span></div></div>
      <div class="card"><div class="shot slab s-walnut" role="img" aria-label="Walnut live edge slab"></div><div class="name">PRODUCT NAME</div><div class="row">$50.00<span class="pill">SHOP NOW</span></div></div>
      <div class="card"><div class="shot slab s-oak" role="img" aria-label="Oak live edge slab"></div><div class="name">PRODUCT NAME</div><div class="row">$50.00<span class="pill">SHOP NOW</span></div></div>
    </div>
    <div class="btn">View All</div>
  </section>

  <!-- shelf 4 -->
  <section class="abs shelf white" style="top:2392px;height:560px">
    <h2>Charcuterie Wood</h2>
    <svg class="rule" viewBox="0 0 216 16"><line x1="0" y1="8" x2="92" y2="8" stroke="#ec5f52" stroke-width="1.5"/><line x1="124" y1="8" x2="216" y2="8" stroke="#ec5f52" stroke-width="1.5"/><circle cx="108" cy="8" r="8" fill="#888"/></svg>
    <svg class="arrow" style="left:52px" viewBox="0 0 28 28"><circle cx="14" cy="14" r="13" fill="#fff" stroke="#ec5f52"/><path d="M18 14H10M13 10l-4 4 4 4" stroke="#ec5f52" stroke-width="1.5" fill="none"/></svg>
    <svg class="arrow" style="left:1118px" viewBox="0 0 28 28"><circle cx="14" cy="14" r="13" fill="#fff" stroke="#ec5f52"/><path d="M10 14h8M15 10l4 4-4 4" stroke="#ec5f52" stroke-width="1.5" fill="none"/></svg>
    <div class="cards">
      <div class="card"><div class="shot s-board1" role="img" aria-label="Pale charcuterie board"></div><div class="name">Charcuterie Wood</div><div class="row">$50.00<span class="pill">SHOP NOW</span></div></div>
      <div class="card"><div class="shot s-board2" role="img" aria-label="Dark charcuterie board"></div><div class="name">Charcuterie Wood</div><div class="row">$50.00<span class="pill">SHOP NOW</span></div></div>
      <div class="card"><div class="shot s-board3" role="img" aria-label="Round handled board"></div><div class="name">Charcuterie Wood</div><div class="row">$50.00<span class="pill">SHOP NOW</span></div></div>
      <div class="card"><div class="shot s-board4" role="img" aria-label="Paddle board"></div><div class="name">Charcuterie Wood</div><div class="row">$50.00<span class="pill">SHOP NOW</span></div></div>
    </div>
    <div class="btn" style="top:454px">View All</div>
  </section>

  <div class="abs video-band"></div>
  <section class="abs video" role="img" aria-label="Worker pouring amber epoxy from a bucket onto a workshop floor">
    <svg class="play" viewBox="0 0 60 60"><circle cx="30" cy="30" r="30" fill="#ec5f52"/><path d="M24 18l18 12-18 12z" fill="#fff"/></svg>
    <p>How To Use Epoxy</p>
  </section>

  <section class="abs testi">
    <h2>Testimonials</h2>
    <h3>What Our Clients Say</h3>
    <svg class="arrow" style="left:242px" viewBox="0 0 28 28"><circle cx="14" cy="14" r="13" fill="#fff" stroke="#ec5f52"/><path d="M18 14H10M13 10l-4 4 4 4" stroke="#ec5f52" stroke-width="1.5" fill="none"/></svg>
    <svg class="arrow" style="left:928px" viewBox="0 0 28 28"><circle cx="14" cy="14" r="13" fill="#fff" stroke="#ec5f52"/><path d="M10 14h8M15 10l4 4-4 4" stroke="#ec5f52" stroke-width="1.5" fill="none"/></svg>
    <blockquote><b>“</b>Lorem ipsum dolor sit amet, consectetur adipiscing elit. In tellus nisi, vulputate in neque ut, lacinia luctus mauris. Nam sed turpis ut nulla rhoncus imperdiet. Sed tempor vestibulum eros sed euismod. Aliquam dapibus neque neque, ultrices vulputate <b>”</b></blockquote>
    <div class="who">N.M. (ACTUAL PATIENT)</div>
    <div class="avatar" role="img" aria-label="Client portrait"></div>
    <div class="dots"><i></i><i></i><i></i><i></i></div>
  </section>

  <footer class="abs footer">
    <div class="brand">Timberpour<br>Studio<i></i></div>
    <div class="follow">Follow Us</div>
    <div class="social" aria-label="Social links"><i></i><i></i><i></i><i></i></div>

    <div class="col" style="left:297px">
      <h4>Quick Links</h4>
      <ul><li>- Home</li><li>- Our Store</li><li>- Our Product</li><li>- Contact Us</li></ul>
      <h4 class="more">Quick More Links</h4>
      <ul><li>- Privacy Policy</li><li>- Terms &amp;</li><li>- Condition</li></ul>
    </div>
    <div class="col" style="left:506px">
      <h4>Category</h4>
      <ul><li>- About Us</li><li>- My courses</li><li>- In person</li><li>- Education</li><li>- Furniture</li><li>- Supplies</li><li>- Wholesale</li><li>- Custom Milling</li><li>- Charcuterie Wood</li><li>- Pre-cut</li></ul>
    </div>
    <div class="col" style="left:706px">
      <h4>Products</h4>
      <ul><li>- Glacier Resin</li><li>- Epoxy</li><li>- Pigments</li><li>- Heron Balm</li><li>- Molds</li><li>- Silicone</li><li>- HDPE</li><li>- Wood</li><li>- Live Edge</li><li>- Ovals &amp; Rounds</li></ul>
    </div>
    <div class="contact">
      <h4>Contact Us</h4>
      <div class="line" style="top:30px"><svg width="24" height="24" viewBox="0 0 24 24"><circle cx="12" cy="12" r="12" fill="#fff"/><path d="M12 19s5-5 5-8a5 5 0 0 0-10 0c0 3 5 8 5 8z" fill="#2e2e2e"/><circle cx="12" cy="11" r="1.8" fill="#fff"/></svg><span>- Your Location Will Be Here Near<br>&nbsp;&nbsp;This Building. 12345</span></div>
      <div class="line" style="top:88px;align-items:center"><svg width="24" height="24" viewBox="0 0 24 24"><circle cx="12" cy="12" r="12" fill="#fff"/><path d="M8 6h3l1 3-2 1a6 6 0 0 0 3 3l1-2 3 1v3a1 1 0 0 1-1 1A10 10 0 0 1 7 7a1 1 0 0 1 1-1z" fill="#2e2e2e"/></svg><span style="font-weight:600;color:#fff">- 1234567890</span></div>
      <div class="line" style="top:144px;align-items:center"><svg width="24" height="24" viewBox="0 0 24 24"><circle cx="12" cy="12" r="12" fill="#fff"/><rect x="6" y="8" width="12" height="8" rx="1" fill="#2e2e2e"/><path d="M6 9l6 4 6-4" stroke="#fff" fill="none"/></svg><span>- info@timberpourstudio.com</span></div>
    </div>
    <div class="copy">©2023 Timberpourstudio. All Rights Reserved.</div>
  </footer>

</div>
</body>
</html>
```